Simple proffessional BC

I have a logo which I will attach below.
I would like the logo on the front of the card with these details in point form below:
Pre and Post Natal Yoga: Pregnancy Workshops: Hypnobirthing Courses
On the back of the card my details:
Merrin Galvey
Facebook page- calmbellieswillowharbour
Mobile- 0438 512 740

I like the idea of the card being simple, possibly just the above on a plain coloured (eggshell?) card, a card that is textured.
I am open to suggestion if it appeals!
Thank you and good luck!

Target Market(s)

Pregnant women, 20's-40's

Requirements
Must have
• Simple, compliment logo.
Make logo the feature.
Should not have

• .

```html
<!DOCTYPE html>
<html lang="en">
<head>
<meta charset="utf-8">
<title>Calm Bellies – Business Card</title>
<link rel="stylesheet" href="https://fonts.googleapis.com/css2?family=Didact+Gothic&family=Mulish:wght@700;800&display=swap">
<style>
  :root {
    --bg: #f1a534;
    --card: #ffffff;
    --orange: #f0960f;
    --maroon: #5c0000;
    --label: #5c0a0a;
  }
  * { box-sizing: border-box; margin: 0; padding: 0; }
  html, body { width: 1200px; height: 1000px; overflow: hidden; }
  body { background: var(--bg); position: relative; font-family: "Didact Gothic", sans-serif; }

  .side-label {
    position: absolute; left: 222px;
    font-family: "Didact Gothic", sans-serif; font-size: 34px; color: var(--label);
  }
  .side-label--back { top: 250px; }
  .side-label--front { top: 690px; }

  .card {
    position: absolute; left: 278px; width: 645px; height: 378px;
    background: var(--card); overflow: hidden;
    box-shadow: 0 4px 14px rgba(120, 60, 0, 0.18);
  }
  .card--back { top: 80px; }
  .card--front { top: 530px; }
  .card svg { position: absolute; inset: 0; }

  /* back */
  .brand-mark {
    position: absolute; top: 58px; left: 0; width: 100%;
    display: flex; align-items: center; justify-content: center; gap: 10px;
  }
  .brand-mark__dot {
    width: 30px; height: 30px; border-radius: 50%; background: var(--orange);
  }
  .brand-mark__name {
    font-family: "Mulish", sans-serif; font-weight: 800; font-size: 22px; color: var(--maroon);
  }
  .holder-name {
    position: absolute; left: 40px; top: 264px;
    font-family: "Mulish", sans-serif; font-weight: 800; font-size: 23px; color: var(--maroon);
  }
  .contact {
    position: absolute; left: 408px; top: 224px; list-style: none;
    font-family: "Mulish", sans-serif; font-weight: 700; font-size: 13px; color: var(--maroon);
    line-height: 25px;
  }

  /* front */
  .wordmark {
    position: absolute; left: 100px; top: 213px;
    display: flex; align-items: center; gap: 12px;
  }
  .wordmark__dot {
    width: 44px; height: 44px; border-radius: 50%; background: var(--orange);
  }
  .wordmark__name {
    font-family: "Didact Gothic", sans-serif; font-size: 30px; color: var(--maroon);
  }
  .services {
    position: absolute; left: 400px; top: 268px; list-style: none;
    font-size: 19px; color: var(--maroon); line-height: 29px;
  }
  .services li { display: flex; align-items: center; gap: 9px; }
  .services li::before {
    content: ""; width: 9px; height: 9px; border-radius: 50%;
    background: radial-gradient(circle at 35% 35%, #e0782a, #8a2a08);
  }
</style>
</head>
<body>

  <span class="side-label side-label--back">B</span>
  <section class="card card--back" aria-label="Card back">
    <svg width="645" height="378" viewBox="0 0 645 378" aria-hidden="true">
      <polygon class="band" fill="var(--orange)"
        points="0,258 382,258 398,214 645,214 645,302 0,302"/>
    </svg>
    <div class="brand-mark">
      <span class="brand-mark__dot"></span>
      <span class="brand-mark__name">Calm Bellies</span>
    </div>
    <h1 class="holder-name">Merrin Galvey</h1>
    <ul class="contact">
      <li>facebook Page : calmbellieswillowharbour</li>
      <li>Mobile : 0438 512 740</li>
    </ul>
  </section>

  <span class="side-label side-label--front">F</span>
  <section class="card card--front" aria-label="Card front">
    <svg width="645" height="378" viewBox="0 0 645 378" aria-hidden="true">
      <g class="stripes stripes--top">
        <rect x="330" y="42" width="315" height="58" fill="var(--maroon)"/>
        <rect x="330" y="68" width="315" height="6" fill="var(--orange)"/>
      </g>
      <g class="stripes stripes--side">
        <rect x="0" y="208" width="86" height="50" fill="var(--maroon)"/>
        <rect x="0" y="230" width="86" height="6" fill="var(--orange)"/>
      </g>
    </svg>
    <div class="wordmark">
      <span class="wordmark__dot"></span>
      <span class="wordmark__name">Calm Bellies</span>
    </div>
    <ul class="services">
      <li>Pre and Post Natal Yoga</li>
      <li>Pregnancy Workshops</li>
      <li>Hypnobirthing Courses</li>
    </ul>
  </section>

</body>
</html>
```